New Flyer Design Project Larkspur Panels and Spaces

Real photos will be added but please start with these for layout. Copy will be supplied so you can just leave a text box to start I am open to suggestions. Thank you

Target Market(s)

Builders, Designers, remodelers, consumers

Colors

Designer to choose colors to be used in the design.

Requirements
Must have
• Before and after photos, email, phone, logo, description

```html
<!DOCTYPE html>
<html lang="en">
<head>
<meta charset="utf-8">
<title>Larkspur Panels and Spaces – Flyer</title>
<link href="https://fonts.googleapis.com/css2?family=Oswald:wght@500;600&family=Arimo:wght@400;700&family=Lato:wght@400;700&display=swap" rel="stylesheet">
<style>
  :root {
    --backdrop: #3e4a53;
    --paper: #ffffff;
    --ink: #333333;
    --ink-soft: #2b2b2b;
    --brand-blue: #1a6bb8;
    --footer-grey: #666666;
    --frame-grey: #9a9a9a;
    --panel-grey: #f1f1f1;
    --wood-a: #8a7661;
    --wood-b: #6d5c4b;
    --plaster-a: #cfcdc8;
    --plaster-b: #9b958c;
    --patina-a: #8c7770;
    --patina-b: #7f9a86;
  }
  * { box-sizing: border-box; margin: 0; padding: 0; }
  html, body { width: 1200px; height: 1200px; overflow: hidden; }
  body { background: var(--backdrop); position: relative; font-family: "Lato", sans-serif; }

  .flyer {
    position: absolute; left: 160px; top: 30px;
    width: 881px; height: 1140px;
    background: var(--paper); overflow: hidden;
  }

  .gallery-frame {
    position: absolute; left: 40px; width: 315px;
    border: 3px solid var(--frame-grey); padding: 4px; background: var(--paper);
  }
  .gallery-frame .photo { width: 100%; height: 100%; }
  .frame-one { top: 27px; height: 265px; }
  .frame-two { top: 311px; height: 265px; }
  .frame-three { top: 595px; height: 264px; }
  .photo-wood { background: linear-gradient(135deg, var(--wood-a), var(--wood-b)); }
  .photo-plaster { background: linear-gradient(135deg, var(--plaster-b), var(--plaster-a) 55%, #e4e2de); }
  .photo-patina { background: linear-gradient(135deg, var(--patina-a), #a08a80 50%, var(--patina-b)); }

  .contact-box {
    position: absolute; left: 42px; top: 872px; width: 309px; height: 195px;
    border: 2px solid var(--brand-blue); background: var(--panel-grey);
    text-align: center; color: var(--ink-soft);
  }
  .contact-title {
    display: inline-block; margin-top: 8px; padding-bottom: 2px;
    font-family: "Oswald", sans-serif; font-weight: 600; font-size: 20px;
    border-bottom: 2px dotted #555;
  }
  .contact-title .accent { color: var(--brand-blue); }
  .contact-lines { font-size: 17px; line-height: 21px; margin-top: 2px; }
  .contact-lines .accent { color: var(--brand-blue); }
  .contact-rule { width: 146px; margin: 8px auto 0; border-top: 2px dotted #555; }
  .contact-phone {
    margin-top: 9px; font-size: 20px; letter-spacing: 0.5px;
    display: flex; align-items: center; justify-content: center; gap: 12px;
  }

  .logo-text {
    position: absolute; left: 390px; width: 450px; top: 30px; text-align: center;
    font-family: "Oswald", sans-serif; font-weight: 600; font-size: 58px;
    color: var(--ink); letter-spacing: 1px;
  }
  .feature-photo { position: absolute; left: 390px; top: 130px; width: 450px; height: 347px; }

  .headline {
    position: absolute; left: 390px; top: 480px;
    font-family: "Oswald", sans-serif; font-weight: 600; font-size: 45px;
    color: var(--brand-blue); letter-spacing: 0.5px;
  }
  .subhead {
    position: absolute; left: 390px; top: 536px;
    font-family: "Arimo", sans-serif; font-size: 39px; color: var(--ink);
  }
  .tagline {
    position: absolute; left: 390px; top: 594px;
    font-family: "Arimo", sans-serif; font-weight: 700; font-size: 27px;
    color: var(--brand-blue); letter-spacing: 0.3px;
  }

  .services-tag { position: absolute; left: 396px; top: 647px; width: 130px; height: 31px; }
  .services-tag span {
    position: absolute; left: 8px; top: 4px; color: #fff;
    font-family: "Lato", sans-serif; font-weight: 700; font-size: 19px;
  }

  .service-item {
    position: absolute; left: 390px; width: 440px;
    display: flex; gap: 12px; align-items: flex-start;
    font-size: 14.5px; line-height: 18px; color: var(--ink-soft);
  }
  .service-item svg { flex: none; margin-top: 3px; }

  .footer { position: absolute; left: 0; top: 1074px; width: 881px; height: 66px; }
  .footer-text {
    position: absolute; color: #fff; font-size: 17px;
    display: flex; align-items: center; gap: 14px;
  }
  .footer-email { left: 105px; top: 24px; }
  .footer-web { left: 512px; top: 28px; }
</style>
</head>
<body>
<main class="flyer">
  <div class="gallery-frame frame-one"><div class="photo photo-wood" role="img" aria-label="Before photo: weathered wooden door panel with wrought iron scroll grille"></div></div>
  <div class="gallery-frame frame-two"><div class="photo photo-plaster" role="img" aria-label="Detail photo: iron strap hinge on a peeling white-painted door"></div></div>
  <div class="gallery-frame frame-three"><div class="photo photo-patina" role="img" aria-label="Detail photo: distressed door panel with pink and green painted patina"></div></div>

  <section class="contact-box">
    <div class="contact-title">Contact us <span class="accent">TODAY</span></div>
    <div class="contact-lines">
      to discuss<br>YOUR PROJECT<br>and receive<br>A <span class="accent">FREE</span> ESTIMATE<br>within <span class="accent">72 hours!</span>
    </div>
    <div class="contact-rule"></div>
    <div class="contact-phone">
      <svg width="18" height="18" viewBox="0 0 24 24" aria-hidden="true"><path d="M6.6 10.8a15 15 0 0 0 6.6 6.6l2.2-2.2c.3-.3.7-.4 1-.2 1.1.4 2.3.6 3.6.6.6 0 1 .4 1 1V20c0 .6-.4 1-1 1A17 17 0 0 1 3 4c0-.6.4-1 1-1h3.5c.6 0 1 .4 1 1 0 1.3.2 2.5.6 3.6.1.3 0 .7-.2 1z" fill="none" stroke="#1a6bb8" stroke-width="2"/></svg>
      <span>0123456789</span>
    </div>
  </section>

  <div class="logo-text">YOUR LOGO</div>
  <div class="feature-photo photo-wood" role="img" aria-label="Featured photo: rustic wooden door with wrought iron diamond scroll grille"></div>

  <h1 class="headline">LOREM IPSUM</h1>
  <h2 class="subhead">Neque porro quisquam</h2>
  <h3 class="tagline">EST QUI DOLOREM IPSUM QUIA</h3>

  <div class="services-tag">
    <svg width="130" height="31" viewBox="0 0 130 31" aria-hidden="true"><polygon points="0,0 116,0 130,31 0,31" fill="#1a6bb8"/></svg>
    <span>SERVICES:</span>
  </div>

  <div class="service-item" style="top:689px"><svg width="14" height="14" viewBox="0 0 14 14" aria-hidden="true"><rect x="1" y="2" width="11" height="11" fill="none" stroke="#1a6bb8" stroke-width="1.4"/><path d="M4 7l2.5 2.5L13 2" fill="none" stroke="#1a6bb8" stroke-width="1.6"/></svg><span>The standard Lorem Ipsum passage, used since the 1500s</span></div>
  <div class="service-item" style="top:717px"><svg width="14" height="14" viewBox="0 0 14 14" aria-hidden="true"><rect x="1" y="2" width="11" height="11" fill="none" stroke="#1a6bb8" stroke-width="1.4"/><path d="M4 7l2.5 2.5L13 2" fill="none" stroke="#1a6bb8" stroke-width="1.6"/></svg><span>Section 1.10.32 of "de Finibus Bonorum et Malorum",<br>written by Cicero in 45 BC</span></div>
  <div class="service-item" style="top:769px"><svg width="14" height="14" viewBox="0 0 14 14" aria-hidden="true"><rect x="1" y="2" width="11" height="11" fill="none" stroke="#1a6bb8" stroke-width="1.4"/><path d="M4 7l2.5 2.5L13 2" fill="none" stroke="#1a6bb8" stroke-width="1.6"/></svg><span>1914 translation by H. Rackham</span></div>
  <div class="service-item" style="top:804px"><svg width="14" height="14" viewBox="0 0 14 14" aria-hidden="true"><rect x="1" y="2" width="11" height="11" fill="none" stroke="#1a6bb8" stroke-width="1.4"/><path d="M4 7l2.5 2.5L13 2" fill="none" stroke="#1a6bb8" stroke-width="1.6"/></svg><span>Section 1.10.33 of "de Finibus Bonorum et Malorum",<br>written by Cicero in 45 BC</span></div>
  <div class="service-item" style="top:856px"><svg width="14" height="14" viewBox="0 0 14 14" aria-hidden="true"><rect x="1" y="2" width="11" height="11" fill="none" stroke="#1a6bb8" stroke-width="1.4"/><path d="M4 7l2.5 2.5L13 2" fill="none" stroke="#1a6bb8" stroke-width="1.6"/></svg><span>1914 translation by H. Rackham</span></div>
  <div class="service-item" style="top:890px"><svg width="14" height="14" viewBox="0 0 14 14" aria-hidden="true"><rect x="1" y="2" width="11" height="11" fill="none" stroke="#1a6bb8" stroke-width="1.4"/><path d="M4 7l2.5 2.5L13 2" fill="none" stroke="#1a6bb8" stroke-width="1.6"/></svg><span>Section 1.10.33 of "de Finibus Bonorum et Malorum",<br>written by Cicero in 45 BC</span></div>
  <div class="service-item" style="top:942px"><svg width="14" height="14" viewBox="0 0 14 14" aria-hidden="true"><rect x="1" y="2" width="11" height="11" fill="none" stroke="#1a6bb8" stroke-width="1.4"/><path d="M4 7l2.5 2.5L13 2" fill="none" stroke="#1a6bb8" stroke-width="1.6"/></svg><span>1914 translation by H. Rackham</span></div>
  <div class="service-item" style="top:970px"><svg width="14" height="14" viewBox="0 0 14 14" aria-hidden="true"><rect x="1" y="2" width="11" height="11" fill="none" stroke="#1a6bb8" stroke-width="1.4"/><path d="M4 7l2.5 2.5L13 2" fill="none" stroke="#1a6bb8" stroke-width="1.6"/></svg><span>Section 1.10.32 of "de Finibus Bonorum et Malorum",<br>written by Cicero in 45 BC</span></div>
  <div class="service-item" style="top:1022px"><svg width="14" height="14" viewBox="0 0 14 14" aria-hidden="true"><rect x="1" y="2" width="11" height="11" fill="none" stroke="#1a6bb8" stroke-width="1.4"/><path d="M4 7l2.5 2.5L13 2" fill="none" stroke="#1a6bb8" stroke-width="1.6"/></svg><span>1914 translation by H. Rackham</span></div>

  <footer class="footer">
    <svg width="881" height="66" viewBox="0 0 881 66" aria-hidden="true">
      <polygon points="0,0 355,0 405,66 0,66" fill="#666666"/>
      <polygon points="372,17 881,17 881,66 410,66" fill="#1a6bb8"/>
    </svg>
    <div class="footer-text footer-email">
      <svg width="17" height="12" viewBox="0 0 17 12" aria-hidden="true"><rect x="0.5" y="0.5" width="16" height="11" fill="#fff"/><path d="M0.5 0.5l8 6 8-6" fill="none" stroke="#666" stroke-width="1.2"/></svg>
      <span>info@yourwebside.com</span>
    </div>
    <div class="footer-text footer-web">
      <svg width="15" height="15" viewBox="0 0 16 16" aria-hidden="true"><circle cx="8" cy="8" r="6.8" fill="none" stroke="#fff" stroke-width="1.4"/><ellipse cx="8" cy="8" rx="3" ry="6.8" fill="none" stroke="#fff" stroke-width="1.2"/><path d="M1.2 8h13.6M2.5 4.5h11M2.5 11.5h11" stroke="#fff" stroke-width="1.1"/></svg>
      <span>www.yourwebside.com</span>
    </div>
  </footer>
</main>
</body>
</html>
```